Beacon Law Stationary - Law Firm

I am looking for a designer who can help me design letterhead and envelopes consistent with our new business cards. Feel free to reach out to me directly at ned@beaconlawgroup.example. Thank you!! Visit beaconlawgroup.example to see our site and the attached files for creative assets.

Target Market(s)

Anyone needing a lawyer

Font styles to use
Other font styles liked:
• Adobe Caslon Pro

Requirements
Must have
• Adobe Caslon Pro font
Full color
Nice to have
• My photo on front along with 2/3 face of camo - see mock up for example of what I have in mind.

American colors - similar to the ones found on my website and gold.

```html
<!DOCTYPE html>
<html lang="en">
<head>
<meta charset="utf-8">
<title>Beacon Law Stationery</title>
<link rel="stylesheet" href="https://fonts.googleapis.com/css2?family=Libre+Caslon+Text:wght@400;700&family=Arimo:wght@400&display=swap">
<style>
  :root{
    --backdrop:#7a7879;
    --navy:#0b2546;
    --gold:#b29f5f;
    --paper:#ffffff;
    --ink:#4a4a4a;
    --mark-faint:#efede6;
    --caslon:"Libre Caslon Text", Georgia, serif;
    --sans:"Arimo", Helvetica, Arial, sans-serif;
  }
  *{box-sizing:border-box;margin:0;padding:0}
  html,body{width:1200px;height:770px;overflow:hidden;background:var(--backdrop)}
  .canvas{position:relative;width:1200px;height:770px}

  /* Letterhead */
  .letterhead{position:absolute;left:94px;top:63px;width:456px;height:643px;background:var(--paper);box-shadow:0 1px 3px rgba(0,0,0,.35)}
  .letterhead__header{position:absolute;left:0;top:0;width:100%;height:90px;background:var(--navy)}
  .rule-gold{position:absolute;left:0;width:100%;height:2px;background:var(--gold)}
  .letterhead .rule-gold{top:91px}
  .brand{position:absolute;display:flex;align-items:center;gap:8px}
  .brand__dot{width:14px;height:14px;border-radius:50%;background:var(--gold)}
  .brand__name{font-family:var(--caslon);color:var(--gold);letter-spacing:.04em;text-transform:uppercase;white-space:nowrap}
  .letterhead .brand{left:46px;top:34px}
  .letterhead .brand__name{font-size:15.5px}
  .contact{position:absolute;left:306px;top:23px;list-style:none;font-family:var(--caslon);font-size:7.6px;color:#fff;line-height:9.5px}
  .contact li{display:flex;gap:5px;align-items:flex-start}
  .contact li+li{margin-top:3px}
  .contact svg{width:7px;height:7px;flex:none;margin-top:1px;fill:var(--gold)}
  .watermark{position:absolute;display:flex;align-items:center;justify-content:center;gap:6px;font-family:var(--caslon);color:var(--mark-faint);text-transform:uppercase;letter-spacing:.05em}
  .letterhead .watermark{left:150px;top:300px;width:148px;font-size:18px}
  .watermark__dot{width:22px;height:22px;border-radius:50%;background:var(--mark-faint);flex:none}
  .letter{position:absolute;left:47px;top:245px;width:360px;font-family:var(--sans);color:var(--ink)}
  .letter__salutation{font-size:9.6px;margin-bottom:13px}
  .letter p{font-size:7.2px;line-height:10.8px;text-align:justify;margin-bottom:10.8px}
  .letter__closing{position:absolute;left:47px;top:463px;font-family:var(--sans);font-size:7.4px;color:var(--ink)}
  .signature{position:absolute;left:47px;top:490px;width:60px;height:24px;background:linear-gradient(90deg,#e9ecf1,#f7f8fa)}
  .letterhead__footer{position:absolute;left:0;top:600px;width:100%;height:18px;background:var(--gold)}
  .practice-areas{position:absolute;left:47px;top:4px;font-family:var(--caslon);font-size:7.6px;color:#fff}
  .badge{position:absolute;top:-5px;width:28px;height:28px;border-radius:50%}
  .badge--one{left:369px;background:#f2f2f4;border:2px solid #2d4f98}
  .badge--two{left:418px;background:#c9a832;border:2px solid #1e3a8a}

  /* Envelope back */
  .envelope-back{position:absolute;left:644px;top:331px;width:508px;height:251px;background:var(--paper);box-shadow:0 1px 3px rgba(0,0,0,.35)}
  .envelope-back__flap{position:absolute;left:0;top:0}
  .envelope-back__seal{position:absolute;left:247px;top:36px;width:14px;height:14px;border-radius:50%;background:var(--gold)}

  /* Envelope front */
  .envelope-front{position:absolute;left:584px;top:454px;width:509px;height:252px;background:var(--paper);box-shadow:0 1px 3px rgba(0,0,0,.35)}
  .envelope-front__header{position:absolute;left:0;top:0;width:100%;height:85px;background:var(--navy)}
  .envelope-front .rule-gold{top:86px}
  .envelope-front .brand{left:32px;top:29px}
  .envelope-front .brand__name{font-size:15px}
  .return-address{position:absolute;left:62px;top:52px;font-family:var(--caslon);font-size:7.6px;line-height:9.6px;color:#fff}
  .envelope-front .watermark{left:420px;top:150px;width:80px;font-size:10px;flex-direction:column}
</style>
</head>
<body>
<main class="canvas">

  <section class="letterhead" aria-label="Letterhead">
    <header class="letterhead__header">
      <div class="brand"><span class="brand__dot"></span><span class="brand__name">Beacon Law</span></div>
      <ul class="contact">
        <li><svg viewBox="0 0 10 10"><path d="M5 0a3.5 3.5 0 0 0-3.5 3.5C1.5 6 5 10 5 10s3.5-4 3.5-6.5A3.5 3.5 0 0 0 5 0zm0 5a1.5 1.5 0 1 1 0-3 1.5 1.5 0 0 1 0 3z"/></svg><span>48 Harbor Lantern Avenue<br>Cedar Point, Florida 32900</span></li>
        <li><svg viewBox="0 0 10 10"><path d="M2 0l2 2.5-1 1.2a6 6 0 0 0 3.3 3.3l1.2-1L10 8l-1.3 1.6C4.5 10 0 5.5.4 1.3z"/></svg><span>(555)014-2290</span></li>
        <li><svg viewBox="0 0 10 10"><path d="M0 2h10v6H0zM0 2l5 3.5L10 2" stroke="#0b2546" stroke-width=".8"/></svg><span>office@beaconlawgroup.example</span></li>
        <li><svg viewBox="0 0 10 10"><circle cx="5" cy="5" r="4.5"/><path d="M.5 5h9M5 .5c-2 2.5-2 6.5 0 9M5 .5c2 2.5 2 6.5 0 9" stroke="#0b2546" stroke-width=".6" fill="none"/></svg><span>www.beaconlawgroup.example</span></li>
      </ul>
    </header>
    <div class="rule-gold"></div>

    <div class="watermark" aria-hidden="true"><span class="watermark__dot"></span><span>Beacon Law</span></div>

    <article class="letter">
      <p class="letter__salutation">Dear Mr. Carter,</p>
      <p>Lorem ipsum dolor sit amet, consectetur adipiscing elit. Donec orci purus, luctus vitae dignissim eu, iaculis sed purus. Vivamus faucibus, ipsum nec aliquet viverra, leo mauris condimentum ligula, sit amet sagittis enim ligula quis arcu. Nam egestas tortor id nisi porttitor mattis. In tortor ante, ultricies in suscipit a, tempus non massa. Vivamus et auctor mi. Fusce vel massa nulla. Phasellus nec eros mauris, et scelerisque orci.</p>
      <p>Donec malesuada orci vitae nulla accumsan porta a id massa. Quisque accumsan iaculis magna sit amet fringilla. Maecenas consequat, magna eget tincidunt semper, odio nibh rutrum mi, id feugiat ante nisi eu risus. Vestibulum nunc orci, rhoncus a placerat in, ultricies in mi. Cras mattis varius eros, vel fringilla nisi suscipit eget. Quisque scelerisque sagittis nulla at porttitor.</p>
      <p>Sed id augue vitae urna euismod commodo aliquet a quam. Pellentesque arcu velit, cursus et malesuada ut, consequat et diam. Nullam erat sem, rhoncus id ullamcorper vitae, rhoncus et arcu. In ultricies ultricies nulla, ut rutrum nisi iaculis at. Donec eu magna a metus ornare faucibus. Fusce aliquet faucibus ultricies. Morbi semper, est id tincidunt gravida, sem arcu adipiscing lacus, ac bibendum nulla leo eu purus. Quisque nec diam sed risus consectetur a ccumsan quis quis nibh. Vestibulum id purus lorem.</p>
    </article>
    <p class="letter__closing">Sincerely,</p>
    <div class="signature" role="img" aria-label="Handwritten signature"></div>

    <footer class="letterhead__footer">
      <p class="practice-areas">Personal Injury • Injunctions • Criminal Defense • Family Law</p>
      <span class="badge badge--one" aria-hidden="true"></span>
      <span class="badge badge--two" aria-hidden="true"></span>
    </footer>
  </section>

  <section class="envelope-back" aria-label="Envelope back">
    <svg class="envelope-back__flap" width="508" height="81" viewBox="0 0 508 81" aria-hidden="true">
      <path d="M0 0H508L496 52Q490 80 462 80H46Q18 80 12 52Z" fill="var(--navy)"/>
    </svg>
    <span class="envelope-back__seal"></span>
  </section>

  <section class="envelope-front" aria-label="Envelope front">
    <header class="envelope-front__header">
      <div class="brand"><span class="brand__dot"></span><span class="brand__name">Beacon Law</span></div>
      <p class="return-address">48 Harbor Lantern Avenue<br>Cedar Point, Florida 32900</p>
    </header>
    <div class="rule-gold"></div>
    <div class="watermark" aria-hidden="true"><span class="watermark__dot"></span><span>Beacon Law</span></div>
  </section>

</main>
</body>
</html>
```